yourSmile Kelvin Grove Business Card

Please design a two sided business card that is Elegant and Professional
Add subtle elegant patterns to suit Spot UV printing/ or raised printing

Name: Dr Marcus L. Avery
Qualification: BDSc (QLD)
Title: Dental Surgeon, Clinical Director
Company: yourSmile Kelvin Grove
Phone: (02) 9376 2258
Address: Shop 5/12-14 Langford Rd Kelvin Grove 2117
email: info@yoursmilekelvingrove.example.au
Facebook: facebook.com/yoursmilekelvingrove

Motto:
Quality dentistry you can trust

Description of services (not compulsory):
Preventative Dentistry | General Dentistry
Cosmetic Dentistry | Teeth Whitening
Crown and Bridge | Root Canal Therapy
Veneers | Clearbrace | Orthodontics
Emergency Dental Care | After Hours

Personalised Treatment Plans
Transparent Fees

Please make sure card is elegant and professional

Target Market(s)

general population, patients,
Dental sales companies, other professions

Industry/Entity Type

Dental Clinic

Contact Information for Business Card

Name: Dr Marcus L. Avery
Qualification: BDSc (QLD)
Phone: (02) 9376 2258
Address: Shop 5/12-14 Langford Rd Kelvin Grove

Motto:

Description of services (not compulsory)

Transparent Fees

Image of dental surgery optional

Please make sure card is elegant and profession

Requirements
Must have
• Logo
• Name, Title (next to name), Business
• Phone, address, facbeook
• Must have stylish design to suit SPOT UV reflective printing
Nice to have
• Subtle elegant patterns which will have Spot UV on them when printed
• Colours to match logo colour
• Description of services
Should not have
• Small fonts that are hard to read
• DO NOT PUT IMAGES OF DENTAL INSTRUMENTS OR TEETH PLEASE

```html
<!DOCTYPE html>
<html lang="en">
<head>
<meta charset="utf-8">
<title>yourSmile Kelvin Grove Business Card</title>
<link rel="stylesheet" href="https://fonts.googleapis.com/css2?family=Lato:wght@400;700;900&display=swap">
<style>
  :root {
    --page: #e9e7e4;
    --card: #1c1c1d;
    --card-edge: #2a2a2b;
    --pattern-a: #232324;
    --pattern-b: #18181a;
    --green: #7dc242;
    --white: #f4f4f4;
    --grey: #b5b5b5;
    --rule: #d8d8d8;
  }
  * { box-sizing: border-box; margin: 0; padding: 0; }
  html, body { width: 1200px; height: 900px; overflow: hidden; }
  body {
    background: var(--page);
    font-family: "Lato", sans-serif;
    display: flex;
    align-items: center;
    justify-content: center;
    gap: 40px;
  }
  .card {
    position: relative;
    width: 560px;
    height: 320px;
    background: var(--card);
    border: 1px solid var(--card-edge);
    border-radius: 6px;
    overflow: hidden;
    box-shadow: 0 10px 30px rgba(0,0,0,.25);
    color: var(--white);
  }
  .spot-uv-pattern {
    position: absolute;
    inset: 0;
    background: radial-gradient(ellipse at 40% 30%, var(--pattern-a), var(--pattern-b) 75%);
  }
  .brand-name {
    position: relative;
    font-weight: 900;
    color: var(--white);
    line-height: 1.05;
    display: flex;
    align-items: center;
    gap: 10px;
  }
  .brand-dot {
    width: 14px; height: 14px;
    border-radius: 50%;
    background: var(--green);
    flex: none;
  }

  /* Front: logo and services */
  .card-front {
    display: flex;
    flex-direction: column;
    align-items: center;
    justify-content: center;
    text-align: center;
    padding: 0 34px;
  }
  .card-front .brand-name { font-size: 34px; margin-bottom: 22px; }
  .services {
    position: relative;
    font-size: 12.5px;
    line-height: 1.55;
    color: var(--grey);
  }
  .services strong { color: var(--white); font-weight: 700; }
  .promises {
    position: relative;
    margin-top: 12px;
    font-size: 13px;
    line-height: 1.45;
    color: var(--green);
    font-weight: 700;
  }

  /* Back: contact details */
  .card-back .brand-name {
    position: absolute;
    left: 36px; top: 104px;
    width: 220px;
    font-size: 28px;
  }
  .contact {
    position: absolute;
    left: 292px; top: 92px;
    width: 250px;
  }
  .contact-name { font-size: 15.5px; font-weight: 700; color: var(--green); }
  .contact-title { font-size: 11px; color: var(--grey); margin-top: 2px; }
  .contact-address { font-size: 13px; font-weight: 700; margin-top: 12px; line-height: 1.3; }
  .contact-list { list-style: none; margin-top: 10px; font-size: 12px; line-height: 1.6; }
  .contact-list li { display: flex; align-items: center; gap: 6px; white-space: nowrap; }
  .contact-icon { width: 12px; height: 12px; flex: none; }
  .motto {
    position: absolute;
    left: 24px; right: 24px; bottom: 30px;
    display: flex;
    align-items: center;
    gap: 12px;
    font-size: 13px;
    color: var(--white);
  }
  .motto::before, .motto::after {
    content: "";
    flex: 1;
    height: 1px;
    background: var(--rule);
  }
</style>
</head>
<body>

  <section class="card card-front">
    <div class="spot-uv-pattern" role="img" aria-label="Subtle spot UV star pattern"></div>
    <div class="brand-name"><span class="brand-dot"></span>yourSmile Kelvin Grove</div>
    <p class="services">
      Preventative Dentistry | <strong>General Dentistry</strong> | Cosmetic Dentistry | <strong>Teeth Whitening</strong> | Crown and Bridge | <strong>Root Canal Therapy</strong> | Veneers | <strong>Clearbrace</strong> | Orthodontics | <strong>Emergency Dental Care</strong> | After Hours
    </p>
    <p class="promises">Personalised Treatment Plans<br>Transparent Fees</p>
  </section>

  <section class="card card-back">
    <div class="spot-uv-pattern" role="img" aria-label="Subtle spot UV star pattern"></div>
    <div class="brand-name"><span class="brand-dot"></span><span>yourSmile Kelvin Grove</span></div>
    <div class="contact">
      <p class="contact-name">Dr Marcus L. Avery BDSc (QLD)</p>
      <p class="contact-title">Dental Surgeon, Clinical Director</p>
      <p class="contact-address">Shop 5/12-14 Langford Rd<br>Kelvin Grove</p>
      <ul class="contact-list">
        <li>
          <svg class="contact-icon" viewBox="0 0 12 12"><rect width="12" height="12" rx="2" fill="#7dc242"/><path d="M3.6 2.6l1.3 1.6-.7.8a5 5 0 002.8 2.8l.8-.7 1.6 1.3-.9 1A6.4 6.4 0 012.6 3.5z" fill="#1c1c1d"/></svg>
          (02) 9376 2258
        </li>
        <li>
          <svg class="contact-icon" viewBox="0 0 12 12"><rect width="12" height="12" rx="2" fill="#7dc242"/><rect x="2.5" y="3.5" width="7" height="5" fill="none" stroke="#1c1c1d" stroke-width="1"/><path d="M2.5 3.5L6 6.5l3.5-3" fill="none" stroke="#1c1c1d" stroke-width="1"/></svg>
          info@yoursmilekelvingrove.example.au
        </li>
        <li>
          <svg class="contact-icon" viewBox="0 0 12 12"><circle cx="6" cy="6" r="6" fill="#3b7be0"/></svg>
          facebook.com/yoursmilekelvingrove
        </li>
      </ul>
    </div>
    <p class="motto">Quality dentistry you can trust</p>
  </section>

</body>
</html>
```